Whitcombe Framing Works - Card Design

I am looking to use the logo designs that you already did for me to develop a business card. I would like the card to have a black background and be double sided. I want white and green logo and text. I have attached an inspiration photo of a look that I like. I would like to use the Vertical Logo attached to take up the full front side of the card. On the back where I have my name and information, I would like to have the horizontal logo or maybe even just the image of the 'A' and trees without the text. I am open, but I am looking for something clean and simple and I want the green to really pop! Additional files can be found under Design #: 40593216

Target Market(s)

Homeowners

Industry/Entity Type

Construction

Contact Information for Business Card

Name: Marcus Pellow, Title: Project Manager, Phone: 831.555.0147, Email: whitcombeframingworks@mailbarn.net, address: 418 Juniper Ln, Felton, CA 95092, Lic# 2046318

Colors
00AB8E
00BBA5
67D7C9
C6EFE9
E9F9F6

Requirements
Nice to have
• I would like to see the logos that I have already got from SketchHarbor, though I am open to new ones

```html
<!DOCTYPE html>
<html lang="en">
<head>
<meta charset="utf-8">
<title>Whitcombe Framing Works – Business Card</title>
<link rel="stylesheet" href="https://fonts.googleapis.com/css2?family=Roboto+Condensed:wght@400;500;700&display=swap">
<style>
  :root {
    --backdrop: #8f9095;
    --card-dark: #222321;
    --card-light: #ffffff;
    --ink: #231f20;
    --ink-soft: #2b2b2b;
    --green: #3bb54a;
    --white: #ffffff;
  }
  * { margin: 0; padding: 0; box-sizing: border-box; }
  html, body {
    width: 1200px;
    height: 1200px;
    overflow: hidden;
    background: var(--backdrop);
    font-family: "Roboto Condensed", Arial, sans-serif;
  }
  .canvas {
    position: relative;
    width: 1200px;
    height: 1200px;
  }
  .card {
    position: absolute;
    left: 190px;
    width: 904px;
    height: 516px;
  }
  .card--front {
    top: 42px;
    background: var(--card-dark);
    display: flex;
    align-items: center;
    justify-content: center;
  }
  .card--back {
    top: 625px;
    background: var(--card-light);
  }
  .brand-name {
    font-family: "Roboto Condensed", Arial, sans-serif;
    font-weight: 700;
    text-transform: uppercase;
    text-align: center;
    line-height: 1.05;
  }
  .card--front .brand-name {
    color: var(--white);
    font-size: 82px;
    letter-spacing: 2px;
  }
  .card--back .brand-name {
    position: absolute;
    left: 40px;
    top: 160px;
    width: 390px;
    color: var(--ink);
    font-size: 48px;
    letter-spacing: 1px;
  }
  .contact {
    position: absolute;
    left: 479px;
    top: 100px;
    color: var(--ink-soft);
  }
  .contact__name {
    font-size: 45px;
    font-weight: 500;
    color: var(--ink);
    line-height: 1;
  }
  .contact__title {
    margin-top: 12px;
    font-size: 23px;
    font-weight: 500;
    letter-spacing: 0.5px;
    color: var(--ink);
  }
  .contact__address {
    margin-top: 26px;
    font-size: 20px;
    line-height: 42px;
  }
  .contact__license { color: var(--green); }
  .contact__lines {
    margin-top: 20px;
    list-style: none;
    font-size: 20px;
  }
  .contact__lines li {
    display: flex;
    align-items: center;
    height: 38px;
  }
  .contact__icon {
    width: 20px;
    height: 20px;
    margin-right: 12px;
    flex: none;
  }
</style>
</head>
<body>
<main class="canvas">
  <section class="card card--front" aria-label="Card front">
    <p class="brand-name">Whitcombe<br>Framing Works</p>
  </section>

  <section class="card card--back" aria-label="Card back">
    <p class="brand-name">Whitcombe<br>Framing Works</p>

    <div class="contact">
      <h1 class="contact__name">Marcus Pellow</h1>
      <p class="contact__title">PROJECT MANAGER</p>
      <p class="contact__address">418 Juniper Ln, Felton,<br>CA 95092, <span class="contact__license">Lic# 2046318</span></p>
      <ul class="contact__lines">
        <li>
          <svg class="contact__icon" viewBox="0 0 24 24" aria-hidden="true">
            <path fill="#231f20" d="M6.6 10.8a15.1 15.1 0 0 0 6.6 6.6l2.2-2.2c.3-.3.7-.4 1-.2 1.1.4 2.3.6 3.6.6.6 0 1 .4 1 1V20c0 .6-.4 1-1 1C10.6 21 3 13.4 3 4c0-.6.4-1 1-1h3.5c.6 0 1 .4 1 1 0 1.3.2 2.5.6 3.6.1.3 0 .7-.2 1L6.6 10.8z"/>
          </svg>
          <span>831.555.0147</span>
        </li>
        <li>
          <svg class="contact__icon" viewBox="0 0 24 24" aria-hidden="true">
            <rect x="2" y="5" width="20" height="14" fill="#231f20"/>
            <path d="M3 6l9 7 9-7" fill="none" stroke="#fff" stroke-width="1.6"/>
          </svg>
          <span>whitcombeframingworks@mailbarn.net</span>
        </li>
        <li>
          <svg class="contact__icon" viewBox="0 0 24 24" aria-hidden="true">
            <g fill="none" stroke="#231f20" stroke-width="1.8">
              <circle cx="12" cy="12" r="9"/>
              <ellipse cx="12" cy="12" rx="4" ry="9"/>
              <path d="M3 12h18M4.5 7.5h15M4.5 16.5h15"/>
            </g>
          </svg>
          <span>www.whitcombeframingworks.net</span>
        </li>
      </ul>
    </div>
  </section>
</main>
</body>
</html>
```